Hollowmere Capital Stationary Design

We have selected a logo as our winner, we now need a full stationary set to be in the same theme.
Required:
- Letter Head
- Business Card Template
- Custom Envelopes
- A5 Notepad Design (Front cover and content pages. Content pages blank(no lines) but with our branding on them,)
- With Compliments Slip
Updates

Hey All,

We have changed the colour scheme of our logo. Our apologies if anyone has begun designing based off the old scheme. Please see the updated scheme in the brief,

Oliver

Target Market(s)

Target market is experienced property developers and financial institutions.

Industry/Entity Type

Commercial Finance

Font styles to use
Serif

Colors
0054AA
0677BA
7BADD7
CADEEF
E8F1F8
0094D4
00A9DD
6FCCEA
C7EBF8
E9F6FB
00AB8E
00BBA5
67D7C9
C6EFE9
E9F9F6
59FF00
82FF00
B8FF75
E3FFCB
F4FFEA

```html
<!DOCTYPE html>
<html lang="en">
<head>
<meta charset="utf-8">
<title>Hollowmere Capital Stationery</title>
<link href="https://fonts.googleapis.com/css2?family=Tinos:wght@400;700&display=swap" rel="stylesheet">
<style>
  :root{
    --brand-blue:#0054AA;
    --brand-teal:#00AB8E;
    --paper:#ffffff;
    --ink:#111111;
    --backdrop:#eceff2;
    --edge:rgba(0,0,0,.12);
  }
  *{box-sizing:border-box;margin:0;padding:0}
  html,body{width:1200px;height:991px;overflow:hidden}
  body{background:var(--backdrop);position:relative;font-family:"Tinos",serif;color:var(--ink)}
  .sheet{position:absolute;background:var(--paper);box-shadow:0 2px 6px var(--edge);overflow:hidden}

  .letterhead{left:31px;top:32px;width:634px;height:896px}
  .card{top:177px;width:269px;height:154px}
  .card--logo{left:66px}
  .card--contact{left:357px}
  .envelope{left:52px;top:553px;width:591px;height:290px}
  .notepad{left:703px;top:32px;width:445px;height:651px;border-radius:0 0 26px 26px}
  .slip{left:703px;top:721px;width:322px;height:153px}

  .brand{position:absolute;display:flex;align-items:center;gap:6px;color:var(--brand-blue);font-weight:700;white-space:nowrap;line-height:1}
  .brand__mark{background:var(--brand-teal);flex:none}

  .contact{position:absolute;line-height:1.2}
  .contact__name{font-size:11px;white-space:nowrap}
  .contact__role{font-size:5.5px;font-weight:700;margin-bottom:3px}
  .contact__line{display:flex;align-items:center;gap:4px;font-size:5.5px;font-weight:700;white-space:nowrap}
  .contact__line svg{width:5px;height:5px;fill:var(--ink);flex:none}

  .rule{position:absolute;left:0;right:0;display:flex}
  .rule .teal{flex:1;background:var(--brand-teal)}
  .rule .blue{flex:1;background:var(--brand-blue)}

  .slip__title{position:absolute;left:14px;top:10px;font-size:17px}
  .slip__from{position:absolute;left:14px;top:85px;font-size:9px}
</style>
</head>
<body>
<svg width="0" height="0" style="position:absolute" aria-hidden="true">
  <symbol id="icon-phone" viewBox="0 0 10 10"><path d="M2 0.5 3.6 2.6 2.7 3.6C3.3 5 5 6.7 6.4 7.3L7.4 6.4 9.5 8 8.5 9.5C4.5 9.2.8 5.5.5 1.5Z"/></symbol>
  <symbol id="icon-mail" viewBox="0 0 10 10"><path d="M0 2h10v6H0Z M0.8 2.6 5 5.6 9.2 2.6" fill-rule="evenodd"/></symbol>
  <symbol id="icon-pin" viewBox="0 0 10 10"><path d="M5 0a3.5 3.5 0 0 1 3.5 3.5C8.5 6 5 10 5 10S1.5 6 1.5 3.5A3.5 3.5 0 0 1 5 0Zm0 2a1.4 1.4 0 1 0 0 2.8A1.4 1.4 0 0 0 5 2Z"/></symbol>
</svg>

<section class="sheet letterhead" aria-label="Letterhead">
  <div class="brand" style="left:80px;top:34px;font-size:17px"><span class="brand__mark" style="width:11px;height:11px"></span>Hollowmere Capital</div>
  <div class="contact" style="left:392px;top:18px">
    <div class="contact__name">First Last name</div>
    <div class="contact__role">Founder</div>
    <div class="contact__line"><svg><use href="#icon-phone"/></svg>+1 555-014-2087</div>
    <div class="contact__line"><svg><use href="#icon-mail"/></svg>www.hollowmere.com</div>
    <div class="contact__line"><svg><use href="#icon-pin"/></svg>your office address will goes here</div>
  </div>
  <div class="rule" style="top:86px;height:12px"><span class="teal"></span><span class="blue"></span></div>
  <div class="rule" style="bottom:8px;height:6px"><span class="blue"></span><span class="teal"></span></div>
</section>

<section class="sheet card card--logo" aria-label="Business card front">
  <div class="brand" style="left:0;right:0;justify-content:center;top:68px;font-size:15px"><span class="brand__mark" style="width:10px;height:10px"></span>Hollowmere Capital</div>
  <div class="rule" style="bottom:0;height:6px"><span class="blue"></span><span class="teal"></span></div>
</section>

<section class="sheet card card--contact" aria-label="Business card back">
  <div class="contact" style="left:10px;top:16px">
    <div class="contact__name">First Last name</div>
    <div class="contact__role">Founder</div>
  </div>
  <div class="brand" style="right:12px;top:18px;font-size:9px"><span class="brand__mark" style="width:6px;height:6px"></span>Hollowmere Capital</div>
  <div class="contact" style="left:10px;top:66px">
    <div class="contact__line"><svg><use href="#icon-phone"/></svg>+1 555-014-2087</div>
    <div class="contact__line"><svg><use href="#icon-mail"/></svg>www.hollowmere.com</div>
    <div class="contact__line"><svg><use href="#icon-pin"/></svg>your office address will goes here</div>
  </div>
  <div class="rule" style="bottom:0;height:6px"><span class="blue"></span><span class="teal"></span></div>
</section>

<section class="sheet envelope" aria-label="Envelope">
  <div class="brand" style="left:32px;top:33px;font-size:15px"><span class="brand__mark" style="width:10px;height:10px"></span>Hollowmere Capital</div>
  <div class="contact" style="left:32px;top:187px">
    <div class="contact__name">First Last name</div>
    <div class="contact__role">Founder</div>
    <div class="contact__line"><svg><use href="#icon-phone"/></svg>+1 555-014-2087</div>
    <div class="contact__line"><svg><use href="#icon-mail"/></svg>www.hollowmere.com</div>
    <div class="contact__line"><svg><use href="#icon-pin"/></svg>your office address will goes here</div>
  </div>
  <div class="rule" style="bottom:0;height:6px"><span class="blue"></span><span class="teal"></span></div>
</section>

<section class="sheet notepad" aria-label="A5 notepad cover">
  <div class="brand" style="left:0;right:0;justify-content:center;top:316px;font-size:24px"><span class="brand__mark" style="width:15px;height:15px"></span>Hollowmere Capital</div>
  <div class="rule" style="bottom:44px;height:8px"><span class="blue"></span><span class="teal"></span></div>
</section>

<section class="sheet slip" aria-label="With compliments slip">
  <div class="slip__title">With Compliments</div>
  <div class="slip__from">From : -</div>
  <div class="brand" style="left:14px;top:109px;font-size:11px"><span class="brand__mark" style="width:7px;height:7px"></span>Hollowmere Capital</div>
  <div class="contact" style="left:198px;top:97px;line-height:2.6">
    <div class="contact__line"><svg><use href="#icon-phone"/></svg>+1 555-014-2087</div>
    <div class="contact__line"><svg><use href="#icon-mail"/></svg>www.hollowmere.com</div>
    <div class="contact__line"><svg><use href="#icon-pin"/></svg>your office address will goes here</div>
  </div>
</section>
</body>
</html>
```